Lume Hart Co Need a custom graphic

I need to have the attached chart re-designed in a hand colored pencil format. The heading needs to be changed to "The most effective methods for hiring sales people". Do not include the background logo in the sample file.

Place the attached Lume Hart Co logo next to the most effective methods (91%)

```html
<!DOCTYPE html>
<html lang="en">
<head>
<meta charset="utf-8">
<title>The Most Effective Methods for Hiring Sales People</title>
<link rel="stylesheet" href="https://fonts.googleapis.com/css2?family=Bebas+Neue&family=Oswald:wght@500;600&family=Montserrat:wght@800&family=Poppins:wght@800&display=swap">
<style>
  :root{
    --stage:#7f7f7f;
    --card:#ffffff;
    --navy:#0c2a6b;
    --sky:#1e9be0;
    --band-light:#e2f4fb;
    --band-dark:#b9e0f0;
    --red:#e8321f;
    --bar-dark-front:#1c3f8a;
    --bar-dark-side:#0f2864;
    --bar-dark-top:#3560ad;
    --bar-light-front:#0b98d8;
    --bar-light-side:#07699d;
    --bar-light-top:#45b8ec;
    --ink:#111111;
    --chevron:#9fb0cf;
  }
  html,body{margin:0;padding:0;width:1200px;height:1040px;overflow:hidden;background:var(--stage);}
  .poster{position:absolute;left:0;top:117px;width:1200px;height:806px;background:var(--card);}
  .poster svg{display:block;}
  .title{font-family:'Bebas Neue',sans-serif;font-size:62px;letter-spacing:0.5px;fill:#fff;}
  .title .accent{fill:var(--sky);}
  .brand{font-family:'Oswald',sans-serif;font-weight:600;font-size:30px;fill:var(--navy);}
  .brand-mark{fill:var(--sky);}
  .band-light{fill:var(--band-light);}
  .band-dark{fill:var(--band-dark);}
  .gridline{stroke:#fff;stroke-width:2.5;}
  .axis{stroke:var(--ink);stroke-width:1.5;fill:none;}
  .tick-label{font-family:'Montserrat',sans-serif;font-weight:800;font-size:17px;fill:var(--ink);text-anchor:end;}
  .bar-dark .front{fill:var(--bar-dark-front);}
  .bar-dark .side{fill:var(--bar-dark-side);}
  .bar-dark .top{fill:var(--bar-dark-top);}
  .bar-light .front{fill:var(--bar-light-front);}
  .bar-light .side{fill:var(--bar-light-side);}
  .bar-light .top{fill:var(--bar-light-top);}
  .trend{fill:none;stroke:var(--red);stroke-width:2;}
  .trend-dot{fill:var(--red);}
  .method-label{font-family:'Oswald',sans-serif;font-weight:600;font-size:14.5px;fill:var(--ink);text-anchor:middle;}
  .pill{fill:var(--red);}
  .pill-text{font-family:'Oswald',sans-serif;font-weight:500;font-size:13.5px;fill:#fff;text-anchor:middle;}
  .axis-arrow{fill:var(--red);}
  .axis-arrow-faint{fill:#f3a79d;}
  .axis-title{font-family:'Montserrat',sans-serif;font-weight:800;font-size:29px;fill:#fff;letter-spacing:0.5px;}
  .method-banner{fill:var(--navy);}
  .method-chevron{fill:var(--chevron);}
  .method-title{font-family:'Poppins',sans-serif;font-weight:800;font-size:29px;fill:#fff;}
</style>
</head>
<body>
<div class="poster">
<svg width="1200" height="806" viewBox="0 0 1250 840" xmlns="http://www.w3.org/2000/svg">
  <!-- header -->
  <polygon fill="#0c2a6b" points="0,0 1250,0 1250,8 1180,102 70,102 0,8"/>
  <polyline points="0,14 67,108 1183,108 1250,14" fill="none" stroke="#0c2a6b" stroke-width="2.5"/>
  <text class="title" x="625" y="84" text-anchor="middle">THE MOST EFFECTIVE METHODS FOR <tspan class="accent">HIRING SALES PEOPLE</tspan></text>

  <!-- brand -->
  <rect class="brand-mark" x="1196" y="136" width="12" height="12"/>
  <text class="brand" x="1188" y="160" text-anchor="end">Lume Hart Co</text>

  <!-- plot bands -->
  <rect class="band-light" x="123" y="170" width="1082" height="473"/>
  <rect class="band-dark" x="123" y="592" width="1082" height="51"/>
  <rect class="band-dark" x="123" y="497" width="1082" height="48"/>
  <rect class="band-dark" x="123" y="401" width="1082" height="48"/>
  <rect class="band-dark" x="123" y="306" width="1082" height="48"/>
  <rect class="band-dark" x="123" y="210" width="1082" height="48"/>

  <g class="gridlines">
    <line class="gridline" x1="215" y1="170" x2="215" y2="643"/>
    <line class="gridline" x1="302" y1="170" x2="302" y2="643"/>
    <line class="gridline" x1="391" y1="170" x2="391" y2="643"/>
    <line class="gridline" x1="478" y1="170" x2="478" y2="643"/>
    <line class="gridline" x1="567" y1="170" x2="567" y2="643"/>
    <line class="gridline" x1="661" y1="170" x2="661" y2="643"/>
    <line class="gridline" x1="744" y1="170" x2="744" y2="643"/>
    <line class="gridline" x1="833" y1="170" x2="833" y2="643"/>
    <line class="gridline" x1="919" y1="170" x2="919" y2="643"/>
    <line class="gridline" x1="1008" y1="170" x2="1008" y2="643"/>
    <line class="gridline" x1="1097" y1="170" x2="1097" y2="643"/>
    <line class="gridline" x1="1191" y1="170" x2="1191" y2="643"/>
  </g>
  <polyline class="axis" points="123,170 123,643 1205,643"/>

  <!-- y ticks -->
  <g>
    <text class="tick-label" x="115" y="646">0.00</text>
    <text class="tick-label" x="115" y="598">0.10</text>
    <text class="tick-label" x="115" y="551">0.20</text>
    <text class="tick-label" x="115" y="503">0.30</text>
    <text class="tick-label" x="115" y="455">0.40</text>
    <text class="tick-label" x="115" y="408">0.50</text>
    <text class="tick-label" x="115" y="360">0.60</text>
    <text class="tick-label" x="115" y="312">0.70</text>
    <text class="tick-label" x="115" y="264">0.80</text>
    <text class="tick-label" x="115" y="217">0.90</text>
  </g>

  <!-- y axis title -->
  <polygon class="axis-arrow-faint" points="36,248 51,232 67,248 67,262 51,246 36,262"/>
  <polygon class="axis-arrow-faint" points="36,262 51,246 67,262 67,276 51,260 36,276"/>
  <polygon class="axis-arrow" points="36,646 36,290 51,274 67,290 67,646"/>
  <text class="axis-title" transform="translate(62,642) rotate(-90)">PREDICTIVE VALIDITY</text>

  <!-- bars -->
  <g class="bar-dark" transform="translate(215,0)"><rect class="front" x="-15" y="621" width="14" height="22"/><polygon class="side" points="-1,621 13,614 13,643 -1,643"/><polygon class="top" points="-15,621 -1,614 13,614 -1,621"/></g>
  <g class="bar-light" transform="translate(302,0)"><rect class="front" x="-15" y="583" width="14" height="60"/><polygon class="side" points="-1,583 13,576 13,643 -1,643"/><polygon class="top" points="-15,583 -1,576 13,576 -1,583"/></g>
  <g class="bar-dark" transform="translate(391,0)"><rect class="front" x="-15" y="564" width="14" height="79"/><polygon class="side" points="-1,564 13,557 13,643 -1,643"/><polygon class="top" points="-15,564 -1,557 13,557 -1,564"/></g>
  <g class="bar-light" transform="translate(478,0)"><rect class="front" x="-15" y="554" width="14" height="89"/><polygon class="side" points="-1,554 13,547 13,643 -1,643"/><polygon class="top" points="-15,554 -1,547 13,547 -1,554"/></g>
  <g class="bar-dark" transform="translate(567,0)"><rect class="front" x="-15" y="535" width="14" height="108"/><polygon class="side" points="-1,535 13,528 13,643 -1,643"/><polygon class="top" points="-15,535 -1,528 13,528 -1,535"/></g>
  <g class="bar-light" transform="translate(661,0)"><rect class="front" x="-15" y="545" width="14" height="98"/><polygon class="side" points="-1,545 13,538 13,643 -1,643"/><polygon class="top" points="-15,545 -1,538 13,538 -1,545"/></g>
  <g class="bar-dark" transform="translate(744,0)"><rect class="front" x="-15" y="487" width="14" height="156"/><polygon class="side" points="-1,487 13,480 13,643 -1,643"/><polygon class="top" points="-15,487 -1,480 13,480 -1,487"/></g>
  <g class="bar-light" transform="translate(833,0)"><rect class="front" x="-15" y="449" width="14" height="194"/><polygon class="side" points="-1,449 13,442 13,643 -1,643"/><polygon class="top" points="-15,449 -1,442 13,442 -1,449"/></g>
  <g class="bar-dark" transform="translate(919,0)"><rect class="front" x="-15" y="363" width="14" height="280"/><polygon class="side" points="-1,363 13,356 13,643 -1,643"/><polygon class="top" points="-15,363 -1,356 13,356 -1,363"/></g>
  <g class="bar-light" transform="translate(1008,0)"><rect class="front" x="-15" y="316" width="14" height="327"/><polygon class="side" points="-1,316 13,309 13,643 -1,643"/><polygon class="top" points="-15,316 -1,309 13,309 -1,316"/></g>
  <g class="bar-dark" transform="translate(1097,0)"><rect class="front" x="-15" y="254" width="14" height="389"/><polygon class="side" points="-1,254 13,247 13,643 -1,643"/><polygon class="top" points="-15,254 -1,247 13,247 -1,254"/></g>
  <g class="bar-light" transform="translate(1191,0)"><rect class="front" x="-15" y="196" width="14" height="447"/><polygon class="side" points="-1,196 13,189 13,643 -1,643"/><polygon class="top" points="-15,196 -1,189 13,189 -1,196"/></g>

  <!-- trend line -->
  <polyline class="trend" points="217,605 290,565 391,544 478,538 567,520 661,532 744,473 833,435 919,350 1008,305 1097,243 1191,183"/>
  <g>
    <circle class="trend-dot" cx="217" cy="605" r="3.5"/><circle class="trend-dot" cx="290" cy="565" r="3.5"/>
    <circle class="trend-dot" cx="391" cy="544" r="3.5"/><circle class="trend-dot" cx="478" cy="538" r="3.5"/>
    <circle class="trend-dot" cx="567" cy="520" r="3.5"/><circle class="trend-dot" cx="661" cy="532" r="3.5"/>
    <circle class="trend-dot" cx="744" cy="473" r="3.5"/><circle class="trend-dot" cx="833" cy="435" r="3.5"/>
    <circle class="trend-dot" cx="919" cy="350" r="3.5"/><circle class="trend-dot" cx="1008" cy="305" r="3.5"/>
    <circle class="trend-dot" cx="1097" cy="243" r="3.5"/><circle class="trend-dot" cx="1191" cy="183" r="3.5"/>
  </g>

  <!-- method labels -->
  <g>
    <text class="method-label" x="215" y="663">CULTURE<tspan x="215" dy="19">TEST</tspan></text>
    <text class="method-label" x="302" y="663">RESUME</text>
    <text class="method-label" x="391" y="663">BEHAVIOR/<tspan x="391" dy="19">PERSONALITY</tspan><tspan x="391" dy="19">TEST</tspan></text>
    <text class="method-label" x="478" y="663">TRADITIONAL<tspan x="478" dy="19">INTERVIEW</tspan></text>
    <text class="method-label" x="567" y="663">REFERENCE<tspan x="567" dy="19">CHECK</tspan></text>
    <text class="method-label" x="661" y="663">EMOTIONAL<tspan x="661" dy="19">INTELLIGENCE</tspan></text>
    <text class="method-label" x="744" y="663">CULTURE<tspan x="744" dy="19">TEST</tspan></text>
    <text class="method-label" x="833" y="663">SKILLS<tspan x="833" dy="19">TEST</tspan></text>
    <text class="method-label" x="919" y="663">GENERAL<tspan x="919" dy="19">MENTAL</tspan><tspan x="919" dy="19">ABILITY</tspan></text>
    <text class="method-label" x="1008" y="663">HIGHLY<tspan x="1008" dy="19">STRUCTURED</tspan><tspan x="1008" dy="19">INTERVIEW</tspan><tspan x="1008" dy="19">WITH</tspan><tspan x="1008" dy="19">SCORECARD</tspan></text>
    <text class="method-label" x="1097" y="663">MULTI<tspan x="1097" dy="19">MEASUREMENT</tspan><tspan x="1097" dy="19">ASSESSMENT</tspan></text>
    <text class="method-label" x="1191" y="663">SALES<tspan x="1191" dy="19">SPECIFIC</tspan><tspan x="1191" dy="19">MULTI</tspan><tspan x="1191" dy="19">MEASUREMENT</tspan><tspan x="1191" dy="19">ASSESSMENT</tspan></text>
  </g>

  <!-- percentage pills -->
  <g>
    <rect class="pill" x="186" y="710" width="56" height="19" rx="9.5"/><text class="pill-text" x="214" y="724">13%</text>
    <rect class="pill" x="275" y="710" width="56" height="19" rx="9.5"/><text class="pill-text" x="303" y="724">18%</text>
    <rect class="pill" x="363" y="710" width="56" height="19" rx="9.5"/><text class="pill-text" x="391" y="724">20%</text>
    <rect class="pill" x="451" y="710" width="56" height="19" rx="9.5"/><text class="pill-text" x="479" y="724">20%</text>
    <rect class="pill" x="540" y="710" width="56" height="19" rx="9.5"/><text class="pill-text" x="568" y="724">23%</text>
    <rect class="pill" x="633" y="710" width="56" height="19" rx="9.5"/><text class="pill-text" x="661" y="724">23%</text>
    <rect class="pill" x="718" y="710" width="56" height="19" rx="9.5"/><text class="pill-text" x="746" y="724">13%</text>
    <rect class="pill" x="804" y="710" width="56" height="19" rx="9.5"/><text class="pill-text" x="832" y="724">33%</text>
    <rect class="pill" x="891" y="710" width="56" height="19" rx="9.5"/><text class="pill-text" x="919" y="724">51%</text>
    <rect class="pill" x="980" y="745" width="56" height="19" rx="9.5"/><text class="pill-text" x="1008" y="759">57%</text>
    <rect class="pill" x="1069" y="745" width="56" height="19" rx="9.5"/><text class="pill-text" x="1097" y="759">71%</text>
    <rect class="pill" x="1162" y="745" width="56" height="19" rx="9.5"/><text class="pill-text" x="1190" y="759">91%</text>
  </g>

  <!-- x axis title -->
  <polygon class="method-chevron" points="420,770 445,770 462,786 445,802 420,802 437,786"/>
  <polygon class="method-chevron" points="437,770 447,770 464,786 447,802 437,802 454,786" opacity="0.6"/>
  <polygon class="method-banner" points="125,770 410,770 427,786 410,802 125,802"/>
  <text class="method-title" x="133" y="797">HIRING METHOD</text>
</svg>
</div>
</body>
</html>
```